Business Cards for Orvanta LLC

We need business cards for a new company called “Orvanta LLC”. This is a technology process improvement company providing a comprehensive assessment of the technology used to run their business. The documentation and review process delivers the visibility and reassurance they need to protect their business and plan for the future. The product is called “Systems Mapwork”. Our primary target is small-medium size businesses, with the deliverables going to the decision maker. We would like to see the designs use the color blue. Our tag line is PROTECT YOUR BUSINESS · TAKE CONTROL OF IT.

Industry/Entity Type

Business

Contact Information for Business Card

Tag line should be on back of card - it does not have to be upper case.

Requirements
Must have
• Please use information when laying out card:
• Name: Gareth Pellham
• Title: Partner
• Phone Number: (844)555-0172
• Email: gareth@orvantallc-example.com
• Website: http://orvantallc-example.com

```html
<!DOCTYPE html>
<html lang="en">
<head>
<meta charset="utf-8">
<title>Business Cards for Orvanta LLC</title>
<link rel="stylesheet" href="https://fonts.googleapis.com/css2?family=Roboto:wght@400;500;700;900&display=swap">
<style>
  :root {
    --bg: #e2e2e2;
    --card: #ffffff;
    --blue: #1f73c2;
    --blue-light: #2a8fd8;
    --blue-dark: #1a64b0;
    --grey: #8c8c8e;
    --grey-light: #a9a9ab;
    --text-dark: #333333;
    --text-mid: #6f6f6f;
  }
  * { box-sizing: border-box; margin: 0; padding: 0; }
  html, body {
    width: 1200px; height: 1000px; overflow: hidden;
    background: var(--bg);
    font-family: "Roboto", Arial, sans-serif;
  }
  .sheet {
    position: relative; width: 1200px; height: 1000px;
  }
  .card {
    position: absolute; left: 210px;
    width: 780px; height: 446px;
    background: var(--card);
    border-radius: 40px;
    overflow: hidden;
    box-shadow: 0 6px 18px rgba(0,0,0,0.18);
  }
  .card--front { top: 36px; }
  .card--back { top: 518px; }

  .wordmark {
    display: flex; align-items: center; gap: 14px;
    color: var(--blue);
    font-weight: 900;
    letter-spacing: 2px;
    text-transform: uppercase;
    line-height: 1;
  }
  .wordmark__square {
    width: 0.8em; height: 0.8em; background: var(--blue); flex: none;
  }
  .card--front .wordmark {
    position: absolute; left: 190px; top: 160px; font-size: 62px;
  }
  .tagline {
    position: absolute; right: 48px; bottom: 92px;
    color: var(--grey-light);
    font-size: 17px; font-weight: 500; letter-spacing: 2px;
  }

  .back-wave { position: absolute; inset: 0; }
  .card--back .wordmark {
    position: absolute; left: 60px; top: 250px; font-size: 40px;
  }
  .contact {
    position: absolute; left: 64px; bottom: 34px;
    list-style: none;
    color: var(--text-mid); font-size: 17px;
  }
  .contact li { display: flex; align-items: center; gap: 14px; height: 28px; }
  .contact svg { width: 16px; height: 16px; fill: var(--blue); flex: none; }
  .contact strong { color: var(--blue); font-weight: 700; }

  .person {
    position: absolute; right: 52px; top: 258px;
    display: flex; align-items: stretch; gap: 12px;
  }
  .person__text { text-align: right; }
  .person__name {
    color: var(--blue); font-size: 24px; font-weight: 700;
    text-transform: uppercase; letter-spacing: 0.5px;
  }
  .person__title {
    color: var(--text-dark); font-size: 13px; font-weight: 700;
    text-transform: uppercase; margin-top: 2px;
  }
  .person__bar { width: 14px; display: flex; flex-direction: column; }
  .person__bar span:first-child { flex: 1; background: var(--blue); }
  .person__bar span:last-child { flex: 1; background: var(--grey); }
</style>
</head>
<body>
<main class="sheet">

  <section class="card card--front" aria-label="Card front">
    <div class="wordmark"><span class="wordmark__square"></span>Orvanta LLC</div>
    <p class="tagline">Protect your business - take control of it.</p>
  </section>

  <section class="card card--back" aria-label="Card back">
    <svg class="back-wave" viewBox="0 0 780 446" aria-hidden="true">
      <defs>
        <linearGradient id="waveBlue" x1="0" y1="1" x2="1" y2="0">
          <stop offset="0" stop-color="#2a8fd8"/>
          <stop offset="1" stop-color="#1a64b0"/>
        </linearGradient>
      </defs>
      <path d="M0 210 C120 150 240 120 360 135 C500 152 640 150 780 95 L780 0 L0 0 Z" fill="url(#waveBlue)"/>
      <path d="M0 250 C120 175 250 140 370 150 C510 162 650 165 780 115 L780 128 C650 180 510 178 370 168 C250 160 120 195 0 272 Z" fill="#8c8c8e"/>
      <path d="M0 300 C100 220 230 175 360 178 C500 182 660 190 780 150 L780 158 C660 200 500 194 360 192 C240 190 110 235 0 312 Z" fill="#a9a9ab"/>
    </svg>

    <div class="wordmark"><span class="wordmark__square"></span>Orvanta LLC</div>

    <div class="person">
      <div class="person__text">
        <p class="person__name">Gareth Pellham</p>
        <p class="person__title">Partner</p>
      </div>
      <div class="person__bar"><span></span><span></span></div>
    </div>

    <ul class="contact">
      <li>
        <svg viewBox="0 0 16 16"><path d="M3 1h3l1.5 4-2 1.3a9 9 0 0 0 4.2 4.2L11 8.5l4 1.5v3a2 2 0 0 1-2 2A13 13 0 0 1 1 3a2 2 0 0 1 2-2z"/></svg>
        <span>(844)555-0172</span>
      </li>
      <li>
        <svg viewBox="0 0 16 16"><path d="M1 3h14v10H1z M1 3l7 6 7-6" fill="none" stroke="#1f73c2" stroke-width="1.6"/></svg>
        <span>gareth@orvantallc-example.com</span>
      </li>
      <li>
        <svg viewBox="0 0 16 16"><circle cx="8" cy="8" r="6.5" fill="none" stroke="#1f73c2" stroke-width="1.6"/><path d="M1.5 8h13M8 1.5c-3 3.5-3 9.5 0 13M8 1.5c3 3.5 3 9.5 0 13" fill="none" stroke="#1f73c2" stroke-width="1.2"/></svg>
        <span>www.<strong>orvantallc-example</strong>.com</span>
      </li>
    </ul>
  </section>

</main>
</body>
</html>
```